Flooring & Interior Design showroom

Just bought this business- Kestrel Lane Flooring & Interiors. Love our logo (we are on Kestrel Lane )and colors
Forest green, gold and black
Love that the back lists everything we do. We no longer have plenotilex but need to add in LVP/ SPC and need to take out vantor shadehub logo at the bottom and use the quib logo instead (maybe? open to suggestions)

Not in love with our cards- I want a higher end look
I hate the gradient poop color we have now.
Would love if they were all black - maybe or ??
or had a foil or embossing?

```html
<!DOCTYPE html>
<html lang="en">
<head>
<meta charset="utf-8">
<title>Kestrel Lane Flooring &amp; Interiors — Business Card</title>
<link rel="stylesheet" href="https://fonts.googleapis.com/css2?family=Open+Sans:wght@400;600;700;800&display=swap">
<style>
  :root {
    --forest: #1f5a34;
    --forest-deep: #16331f;
    --gold: #d9c27e;
    --gold-text: #c9a85a;
    --black: #111211;
    --ink: #1d1d1d;
    --paper: #ffffff;
    --light: #f1efe8;
    --backdrop: #eeeeef;
  }
  * { box-sizing: border-box; margin: 0; padding: 0; }
  html, body { width: 972px; height: 1200px; overflow: hidden; }
  body {
    background: var(--backdrop);
    font-family: "Open Sans", Arial, sans-serif;
    color: var(--ink);
  }
  .card {
    position: absolute;
    left: 76px;
    width: 820px;
    height: 469px;
    box-shadow: 0 6px 22px rgba(0,0,0,0.12);
    overflow: hidden;
  }
  .card--front { top: 92px; background: var(--paper); }
  .card--back { top: 641px; background: var(--black); }

  /* business name set as plain text */
  .brand { position: absolute; display: flex; align-items: center; gap: 12px; }
  .brand__mark { width: 16px; height: 16px; background: var(--forest); flex: none; }
  .brand__name { font-family: "Open Sans", Arial, sans-serif; font-size: 30px; font-weight: 700; line-height: 1.2; white-space: nowrap; }

  .card--front .brand { left: 46px; top: 84px; }
  .card--front .brand__name { color: var(--forest); }

  .person { position: absolute; right: 46px; top: 222px; text-align: right; }
  .person__name { font-size: 42px; font-weight: 800; color: var(--forest); letter-spacing: 2px; line-height: 1; }
  .person__title { font-size: 21px; font-weight: 600; color: var(--ink); margin-top: 4px; }
  .rule { position: absolute; left: 46px; top: 291px; width: 535px; height: 2px; background: var(--gold); }

  .contact { position: absolute; top: 332px; font-size: 21px; line-height: 30px; list-style: none; }
  .contact--left { left: 46px; }
  .contact--right { right: 46px; }
  .contact li { display: flex; align-items: center; gap: 10px; }
  .contact svg { width: 16px; height: 16px; fill: var(--forest); flex: none; }
  .contact .license { color: var(--forest); font-weight: 700; }

  .card--back .brand { left: 0; right: 0; top: 150px; justify-content: center; }
  .card--back .brand__name { color: var(--light); }
  .slogan { position: absolute; left: 0; right: 0; top: 245px; text-align: center; color: var(--gold-text); font-size: 19px; }
  .services {
    position: absolute; left: 0; right: 0; top: 299px; height: 90px;
    background: var(--gold); color: var(--forest-deep);
    font-size: 17.5px; font-weight: 700; line-height: 22px;
    text-align: center; padding-top: 11px; letter-spacing: 0.3px;
  }
  .footer {
    position: absolute; left: 0; right: 0; top: 389px; height: 80px;
    background: var(--forest-deep); color: var(--light);
    display: flex; align-items: center; justify-content: space-between; padding: 0 46px;
  }
  .footer__web { display: flex; align-items: center; gap: 8px; font-size: 21px; }
  .footer__web svg { width: 14px; height: 14px; }
  .partners { display: flex; gap: 26px; font-size: 20px; font-weight: 700; }
  .partner { display: flex; align-items: center; gap: 7px; }
  .partner__dot { width: 16px; height: 16px; border-radius: 50%; background: var(--light); }
  .partner__dot--gold { background: var(--gold); }
</style>
</head>
<body>

<section class="card card--front" aria-label="Card front">
  <div class="brand">
    <span class="brand__mark"></span>
    <span class="brand__name">Kestrel Lane Flooring &amp; Interiors</span>
  </div>

  <div class="person">
    <div class="person__name">MARA LINDQVIST</div>
    <div class="person__title">Owner/ Designer</div>
  </div>
  <div class="rule"></div>

  <ul class="contact contact--left">
    <li><svg viewBox="0 0 16 16"><path d="M8 0a5.5 5.5 0 0 0-5.5 5.5C2.5 10 8 16 8 16s5.5-6 5.5-10.5A5.5 5.5 0 0 0 8 0zm0 7.6a2.1 2.1 0 1 1 0-4.2 2.1 2.1 0 0 1 0 4.2z"/></svg>872 Kestrel Ln., Harbor Cove, CA 90417</li>
    <li><svg viewBox="0 0 16 16"><path d="M1 3h14v1.2L8 9 1 4.2z M1 5.6l7 4.8 7-4.8V13H1z"/></svg>mara@kestrellaneflooring</li>
    <li class="license">CA Lic #581904</li>
  </ul>

  <ul class="contact contact--right">
    <li><svg viewBox="0 0 16 16"><path d="M4 1l2.5 3.5-1.4 1.6c.8 1.8 2.2 3.2 4 4l1.6-1.4L14 11.2 12.5 14C7 13.5 2.5 9 2 3.5z"/></svg>555.210.4471</li>
    <li><svg viewBox="0 0 16 16"><path d="M4 1h8v14H4zm1.5 1.5v9h5v-9z"/></svg>555.384.9026</li>
    <li><svg viewBox="0 0 16 16"><path d="M4 2h7v3H4zM2 6h12v8H2zm2 2v2h8V8z"/></svg>555.619.3380</li>
  </ul>
</section>

<section class="card card--back" aria-label="Card back">
  <div class="brand">
    <span class="brand__mark"></span>
    <span class="brand__name">Kestrel Lane Flooring &amp; Interiors</span>
  </div>
  <p class="slogan">Home Town Service since 1979</p>

  <div class="services">
    AREA RUGS • BLINDS • CARPET • CORK • HARDWOOD • LAMINATE<br>
    SHEERS • VALANCES • VINYL • BED SPREADS • DRAPERIES • LVP/ SPC • FABRIC<br>
    MOTORIZED SHADES • PILLOWS • SHUTTERS • UPHOLSTERY • VERTICALS
  </div>

  <div class="footer">
    <div class="footer__web">
      <svg viewBox="0 0 16 16" fill="none" stroke="#f1efe8" stroke-width="1.4"><circle cx="8" cy="8" r="6.5"/><path d="M1.5 8h13M8 1.5c-3 3.5-3 9.5 0 13M8 1.5c3 3.5 3 9.5 0 13"/></svg>
      kestrellaneflooring.com
    </div>
    <div class="partners">
      <span class="partner">Halbrook Shades<span class="partner__dot"></span></span>
      <span class="partner">quib<span class="partner__dot partner__dot--gold"></span></span>
    </div>
  </div>
</section>

</body>
</html>
```